Compelling Home Page for Clip Harbor Partners

We are a Video SEO specialist that get websites on top of the front page of Zentrova and FlickBarn with video thumbprints that generate great traffic. Video SEO is all we do

see what we're offering at a salespage www.plumfieldreels.example. However, please omit "guarantee"

he home page should introduce our company as a premier company for helping brands get their videos on the front page of zentrova and high up in flickbarn. Should incorporate video "thumbnails" as part of the design. These could be the "triangular click buttons" or little video screens you see as "thumbnails" Needs a prominent place for a video about videoSEO. on Left side of page towards the top.

Needs buttons across the top for other pages. See www.brastonclips.example for frame of reference we want to be better than them.

Must incorporate our logo. We'd like to see the logo on dark background as well as white background.

Simple but with bright and vibrant highlights that look sophisticated, cutting edge and accountable. Shows credentials. Links with examples of thumbnails that are on the front page

We want to beat www.brastonclips.example check it out for point of reference

Target Market(s)

large corporations who have videos already and want to get better traction. Marlow 500. Advertising Agencies for Marlow 500's

Requirements
Must have
• Incorporate our logo. clean, easy to read

```html
<!DOCTYPE html>
<html lang="en">
<head>
<meta charset="utf-8">
<title>Clip Harbor Partners – Video SEO</title>
<link rel="stylesheet" href="https://fonts.googleapis.com/css2?family=Arimo:wght@400;700&family=Arvo&family=Gelasio:ital@0;1&family=Open+Sans:wght@400;600&display=swap">
<style>
:root{
  --header-dark:#0b0b0b;
  --header-mid:#1c1c1c;
  --accent-orange:#f6a80f;
  --brand-blue:#1a6cc0;
  --navy:#1b3a5e;
  --text-dark:#333;
  --text-body:#4a4a4a;
  --panel:#efece8;
  --field:#1d1d1d;
  --send-green:#2f8f2a;
  --teal:#1f8fb0;
  --footer-bar:#e3e3e3;
  --faint:#cfcfcf;
}
*{box-sizing:border-box;margin:0;padding:0}
html,body{width:1200px;height:1016px;overflow:hidden}
body{position:relative;background:#fff;font-family:"Open Sans",Verdana,sans-serif;color:var(--text-body)}
.abs{position:absolute}

/* header */
.site-header{left:0;top:0;width:1200px;height:94px;background:linear-gradient(var(--header-mid),var(--header-dark))}
.brand-mark{left:163px;top:10px;width:70px;height:70px;border-radius:50%;background:var(--accent-orange)}
.brand-name{left:246px;top:33px;font-family:"Arimo",Arial,sans-serif;font-size:28px;color:#fff;letter-spacing:-0.5px;white-space:nowrap}
.main-nav{left:631px;top:35px;display:flex;font-family:"Arimo",Arial,sans-serif;font-size:17px}
.main-nav a{color:#fff;text-decoration:none;padding:4px 10px;margin-right:7px;height:28px;line-height:20px;border:1px solid transparent;border-radius:3px}
.main-nav a.is-current{color:var(--accent-orange);border-color:#5a4a20;background:#161209}

/* hero */
.hero{left:0;top:94px;width:1200px;height:468px;background:radial-gradient(ellipse at 30% 0%,#bfe3ef 0%,#d9eff6 35%,#fff 75%);border-bottom:2px solid #bcd9e8}
.hero-title{left:160px;top:200px;font-family:"Arimo",Arial,sans-serif;font-size:66px;color:var(--brand-blue);white-space:nowrap;letter-spacing:1px}
.hero-dot{left:437px;top:223px;width:44px;height:44px;border-radius:50%;background:var(--brand-blue)}
.hero-lead{left:164px;top:292px;font-family:"Arvo",Georgia,serif;font-size:26px;color:var(--text-dark)}
.hero-lead sup{font-size:13px}
.hero-sub{left:164px;top:331px;font-family:"Arvo",Georgia,serif;font-size:19px;color:var(--text-dark)}
.hero-small{left:165px;top:358px;font-family:"Arvo",Georgia,serif;font-size:14px;color:var(--text-dark)}
.slide-pager{left:162px;top:485px;display:flex;gap:9px;font-family:"Arimo",Arial,sans-serif;font-size:15px;color:var(--navy)}
.slide-pager span{width:20px;height:20px;line-height:20px;text-align:center}
.slide-pager .is-current{background:var(--brand-blue);color:#fff;border-radius:50%;box-shadow:0 0 0 2px #0c3e75}
.hero-screen{left:635px;top:116px;width:393px;height:394px;border-radius:14px;background:linear-gradient(#2a2a2a 0%,#f4f6f8 8%,#e6e9ec 62%,#b8bcc0 80%,#e8e8e8 100%)}

/* content */
.content{left:0;top:563px;width:1200px;height:292px;background:var(--panel)}
.col-title{font-family:"Gelasio",Georgia,serif;font-size:16px;color:#222;white-space:nowrap}
.col-sub{font-family:"Gelasio",Georgia,serif;font-style:italic;font-size:10px;color:#777}
.about-text{left:164px;top:664px;width:324px;font-size:10.6px;line-height:18.5px;text-align:justify;letter-spacing:.3px}
.btn-learn{left:164px;top:805px;width:95px;height:24px;border:1px solid #c8c8c8;border-radius:3px;background:linear-gradient(#fff,#e8e8e8);font-size:9px;letter-spacing:1px;text-align:center;line-height:22px;color:#444}
.divider{width:0;border-left:1px dashed #bdb8b0}
.field{left:512px;width:221px;background:var(--field);color:#bbb;font-size:8px;letter-spacing:.8px;padding:5px 4px}
.btn-send{left:689px;top:815px;width:44px;height:19px;background:var(--send-green);color:#fff;font-size:8px;letter-spacing:1px;text-align:center;line-height:19px}
.example-nav{left:947px;top:634px;font-family:"Gelasio",Georgia,serif;font-size:11px;color:var(--teal);white-space:nowrap}
.example-video{left:776px;top:666px;width:254px;height:164px;border:3px solid #555;border-radius:7px;background:linear-gradient(135deg,#1c3a5a 0%,#3a6688 40%,#a02020 75%,#1c2a3a 100%)}
.play-btn{left:881px;top:720px;width:44px;height:44px;background:rgba(0,0,0,.85);border-radius:4px}

/* updates bar */
.updates-bar{left:0;top:855px;width:1200px;height:45px;background:linear-gradient(#fff,var(--footer-bar));border-top:1px solid #ddd}
.updates-label{left:163px;top:872px;font-size:10px;color:#333}
.updates-input{left:221px;top:870px;width:119px;height:16px;border:1px solid #bbb;background:#f2f2f2;font-size:10px;color:#888;padding-left:4px;line-height:14px}
.btn-go{left:346px;top:870px;width:26px;height:15px;border-radius:8px;background:#222;color:#fff;font-size:8px;text-align:center;line-height:15px;letter-spacing:1px}
.connect-label{left:826px;top:874px;font-family:"Arimo",Arial,sans-serif;font-weight:700;font-size:9.5px;color:#333;letter-spacing:.3px}
.social{top:869px;width:19px;height:19px;border-radius:3px;background:#6f6f6f}

/* footer */
.footer-nav{left:164px;top:917px;font-size:9px;letter-spacing:1px;color:#333;white-space:nowrap;word-spacing:3px}
.footer-contact{left:164px;top:945px;font-size:10.5px;font-weight:600;color:#333;letter-spacing:.5px;white-space:nowrap}
.footer-contact a{color:var(--teal)}
.copyright{left:164px;top:965px;font-size:8.5px;color:#444;letter-spacing:.5px}
.footer-mark{left:755px;top:928px;width:40px;height:40px;border-radius:50%;background:var(--faint)}
.footer-name{left:802px;top:932px;font-family:"Arimo",Arial,sans-serif;font-size:25px;color:var(--faint);white-space:nowrap;letter-spacing:-0.5px}
</style>
</head>
<body>

<header class="abs site-header"></header>
<div class="abs brand-mark"></div>
<div class="abs brand-name">Clip Harbor Partners</div>
<nav class="abs main-nav">
  <a class="is-current" href="#">Home</a>
  <a href="#">Services</a>
  <a href="#">Examples</a>
  <a href="#">Order</a>
  <a href="#">Contact Us</a>
</nav>

<section class="abs hero"></section>
<h1 class="abs hero-title">Video Seo</h1>
<div class="abs hero-dot"></div>
<p class="abs hero-lead">1<sup>st</sup> page video listing on Zentrova</p>
<p class="abs hero-sub">for the Keywords of Your Choice</p>
<p class="abs hero-small">For More Traffic, Leads, and Sales to Your Site!</p>
<div class="abs slide-pager"><span class="is-current">1</span><span>2</span><span>3</span><span>4</span></div>
<div class="abs hero-screen" role="img" aria-label="Desktop computer showing a search results page with a video listing highlighted"></div>

<section class="abs content"></section>

<svg class="abs" style="left:163px;top:619px" width="20" height="26" viewBox="0 0 20 26" aria-hidden="true">
  <rect x="1" y="3" width="18" height="22" rx="2" fill="#1f8fb0"/>
  <rect x="6" y="0" width="8" height="5" rx="1" fill="#16708c"/>
  <path d="M5 10h10M5 14h10M5 18h10" stroke="#fff" stroke-width="1.5"/>
</svg>
<div class="abs col-title" style="left:198px;top:618px">What is Clip Harbor Partners ?</div>
<div class="abs col-sub" style="left:199px;top:637px">who are we?</div>
<p class="abs about-text">Lorem Ipsum is simply dummy text of the printing and typesetting industry. Lorem Ipsum has been the industry's standard dummy text ever since the 1500s, when an unknown printer took a galley of type and scrambled it to make a type specimen book. It has survived not only five centuries, but also the leap into electronic typesetting, remaining essentially unchanged.</p>
<div class="abs btn-learn">LEARN MORE</div>

<div class="abs divider" style="left:497px;top:630px;height:196px"></div>

<svg class="abs" style="left:511px;top:621px" width="28" height="20" viewBox="0 0 28 20" aria-hidden="true">
  <path d="M2 1h24a1 1 0 0 1 1 1v12a1 1 0 0 1-1 1H9l-5 4v-4H2a1 1 0 0 1-1-1V2a1 1 0 0 1 1-1z" fill="#1f8fb0"/>
  <path d="M6 6h16M6 10h12" stroke="#fff" stroke-width="1.5"/>
</svg>
<div class="abs col-title" style="left:548px;top:618px">Send us a Message</div>
<div class="abs col-sub" style="left:549px;top:637px">keep in touch</div>
<div class="abs field" style="top:667px;height:21px">Your Name</div>
<div class="abs field" style="top:695px;height:21px">Your Phone Number</div>
<div class="abs field" style="top:727px;height:21px">Email Address</div>
<div class="abs field" style="top:757px;height:43px">Your Enquiry</div>
<div class="abs btn-send">SEND</div>

<div class="abs divider" style="left:756px;top:630px;height:196px"></div>

<svg class="abs" style="left:778px;top:621px" width="22" height="22" viewBox="0 0 22 22" aria-hidden="true">
  <g fill="#1f8fb0"><circle cx="11" cy="11" r="7"/>
    <rect x="9" y="0" width="4" height="22"/><rect x="0" y="9" width="22" height="4"/>
    <rect x="9" y="0" width="4" height="22" transform="rotate(45 11 11)"/><rect x="9" y="0" width="4" height="22" transform="rotate(-45 11 11)"/></g>
  <circle cx="11" cy="11" r="3.5" fill="#efece8"/>
</svg>
<div class="abs col-title" style="left:810px;top:618px">Examples</div>
<div class="abs col-sub" style="left:811px;top:637px">what we done yet?</div>
<div class="abs example-nav">
  <svg width="8" height="12" viewBox="0 0 8 12" style="vertical-align:-2px"><path d="M7 1 2 6l5 5" stroke="#1f8fb0" stroke-width="2.5" fill="none"/></svg>
  Next&nbsp; | &nbsp;Prev
  <svg width="8" height="12" viewBox="0 0 8 12" style="vertical-align:-2px"><path d="M1 1l5 5-5 5" stroke="#1f8fb0" stroke-width="2.5" fill="none"/></svg>
</div>
<div class="abs example-video" role="img" aria-label="Example client video still: camera operator filming in a studio"></div>
<div class="abs play-btn"></div>
<svg class="abs" style="left:896px;top:732px" width="18" height="20" viewBox="0 0 18 20" aria-hidden="true"><path d="M1 1l16 9-16 9z" fill="#fff"/></svg>

<div class="abs updates-bar"></div>
<div class="abs updates-label">Get Updates</div>
<div class="abs updates-input">Enter your email</div>
<div class="abs btn-go">GO</div>
<div class="abs connect-label">CONNECT WITH US</div>
<div class="abs social" style="left:918px"></div>
<div class="abs social" style="left:948px"></div>
<div class="abs social" style="left:978px"></div>
<div class="abs social" style="left:1010px"></div>

<nav class="abs footer-nav">HOME &nbsp;| &nbsp;SERVICES &nbsp;| &nbsp;EXAMPLES &nbsp;| &nbsp;ORDER &nbsp;| &nbsp;CONTACT US</nav>
<p class="abs footer-contact"><a href="#">Questions or Comments?</a>&nbsp; Call us at 1.800.555.0142 or <a href="#">Email Us</a></p>
<p class="abs copyright">© 2011 Clip Harbor Partners - Privacy Policy</p>
<div class="abs footer-mark"></div>
<div class="abs footer-name">Clip Harbor Partners</div>

</body>
</html>
```